Organic Ready Meal/Food Packaging Design

We are looking to re-vamp/re-design our current food packaging. The design will be for an outer box surround for our food which is packed into plastic pots. The meals are fresh and ready to eat. There are 4 variants (recipes) and one design is needed with a background colour change for each recipe. I am looking for a fresh, modern and eye-catching look which stands out on a supermarket shelf. It should be noted that there there is an existing design which needs an overhaul. I would like the winning bidder to look at this together with some other types of packaging I like to improve it.

I have attached a copy of my existing packaging which can also be seen on our company website www.thebrimfieldkitchen.com. We need to move away from this bitty, wishy washy theme to something brighter and bolder, more modern and innovative like the 'Tub o'' example I have also attached. Other points of reference are www.harlowtarts.co.uk and www.figsprout.co.uk which are bright and eye-catching. The Harlow Tarts 'tub o'' boxes are a good benchmark for us although we do not want to copy the design.

This project probably needs to incorporate a modified company logo and the budget can be modified to include this.

We also need to use the word 'Yummy' as a sub-header for our meals i.e.

Yummy
Organic Mediterranean Bean Casserole

Any other questions, please ask at any time.

Target Market(s)

anybody wanting a healthy, organic ready meal
men
women
mums

Industry/Entity Type

It Company

Requirements
Must have
• Bold modern colours/design
Modern eye catching design/fonts
Should not have
• Illustrations (sketchy drawings)

```html
<!DOCTYPE html>
<html lang="en">
<head>
<meta charset="utf-8">
<title>The Brimfield Kitchen – Box Surround</title>
<link href="https://fonts.googleapis.com/css2?family=Josefin+Sans:wght@300;400&family=Manrope:wght@300;400;500;600;700&display=swap" rel="stylesheet">
<style>
  :root {
    --ink: #060606;
    --orange: #f06b31;
    --paper: #ffffff;
  }
  html, body {
    margin: 0;
    padding: 0;
    width: 1200px;
    height: 900px;
    overflow: hidden;
    background: var(--paper);
  }
  p, h1 { margin: 0; }
  .canvas {
    position: relative;
    width: 1200px;
    height: 900px;
  }
  .tab, .panel { position: absolute; }
  .tab-top { left: 442px; top: 69px; width: 310px; height: 40px; background: var(--ink); }
  .panel-brand { left: 239px; top: 108px; width: 716px; height: 343px; background: var(--ink); }
  .panel-recipe { left: 239px; top: 460px; width: 716px; height: 331px; background: var(--orange); }
  .tab-bottom { left: 442px; top: 790px; width: 310px; height: 40px; background: var(--orange); }

  .tagline {
    position: absolute;
    left: 0; right: 0; top: 58px;
    text-align: center;
    color: var(--orange);
    font-family: "Manrope", sans-serif;
    font-size: 15px;
    line-height: 21px;
  }
  .tagline .en { letter-spacing: 1.4px; }

  .brand-name {
    position: absolute;
    left: 0; right: 0; top: 152px;
    text-align: center;
    white-space: nowrap;
    color: var(--paper);
    font-family: "Josefin Sans", sans-serif;
    font-weight: 300;
    font-size: 46px;
    letter-spacing: 1px;
    text-transform: uppercase;
    line-height: 60px;
  }

  .produce-band {
    position: absolute;
    left: 36px; top: 242px;
    width: 630px; height: 83px;
    background: linear-gradient(90deg, #e9652d, #f27436 50%, #e9652d);
    border-radius: 4px;
  }

  .recipe-text {
    position: absolute;
    left: 37px; top: 47px;
    color: var(--ink);
    font-family: "Manrope", sans-serif;
  }
  .recipe-greek {
    font-size: 20px;
    font-weight: 500;
    line-height: 28px;
  }
  .recipe-sub {
    margin-top: 28px;
    font-family: "Josefin Sans", sans-serif;
    font-weight: 400;
    font-size: 22px;
    line-height: 30px;
    text-transform: uppercase;
  }
  .recipe-name {
    margin-top: 4px;
    font-size: 18px;
    font-weight: 700;
    line-height: 30px;
    text-transform: uppercase;
  }

  .organic-seal {
    position: absolute;
    left: 522px; top: 111px;
    width: 148px; height: 148px;
    box-sizing: border-box;
    border: 5px solid var(--paper);
    border-radius: 50%;
    color: var(--paper);
    font-family: "Manrope", sans-serif;
    text-align: center;
  }
  .seal-figure {
    margin-top: 20px;
    font-size: 30px;
    font-weight: 300;
    line-height: 36px;
  }
  .seal-greek {
    margin-top: 6px;
    font-size: 15px;
    line-height: 19px;
  }
  .seal-en {
    font-size: 14px;
    letter-spacing: 1.2px;
    line-height: 19px;
  }
</style>
</head>
<body>
<main class="canvas">
  <div class="tab tab-top"></div>

  <section class="panel panel-brand">
    <p class="tagline"><span class="gr">Φρέσκα Βιολογικά Τρόφιμα</span><br><span class="en">FRESH ORGANIC FOOD</span></p>
    <h1 class="brand-name">The Brimfield Kitchen</h1>
    <div class="produce-band" role="img" aria-label="Row of flat orange food motifs: wheat stalks, carrots, fish and a small bird"></div>
  </section>

  <section class="panel panel-recipe">
    <div class="recipe-text">
      <p class="recipe-greek">Μακαρόνια με<br>Κοτόπουλο και<br>Ψητά Λαχανικά</p>
      <p class="recipe-sub">Brimfield Organic</p>
      <p class="recipe-name">Red Lentil &amp;<br>Vegetable Soup</p>
    </div>
    <div class="organic-seal">
      <p class="seal-figure">100%</p>
      <p class="seal-greek">Βιολογικό</p>
      <p class="seal-en">ORGANIC</p>
    </div>
  </section>

  <div class="tab tab-bottom"></div>
</main>
</body>
</html>
```